PHD-project

i need the figures to be in the same stile. info is inside the file. There are 5 figures that need redesign. this is for PhD.

Target Market(s)

it will be used in my phd

Colors

Designer to choose colors to be used in the design.

```html
<!DOCTYPE html>
<html lang="en">
<head>
<meta charset="utf-8">
<title>PhD Research Figures</title>
<link rel="stylesheet" href="https://fonts.googleapis.com/css2?family=Montserrat:wght@600;700;800&family=Roboto:wght@400;500;700&display=swap">
<style>
  :root{
    --navy:#2b2d7a;
    --ink:#1d1d1f;
    --red:#e8202a;
    --blue:#2d9fe0;
    --blue-light:#b9ddf3;
    --blue-pale:#dceefa;
    --yellow:#f3c512;
    --orange:#f29a1c;
    --green:#5fc628;
    --cyan:#22aee9;
    --purple:#7d1fae;
    --pink:#e2509f;
    --frame:#2f348e;
    --deep:#14507c;
    --muted:#9a96b8;
  }
  html,body{margin:0;padding:0;width:1200px;height:1108px;overflow:hidden;background:#fff;}
  .canvas{display:block;width:1200px;height:1108px;}
  .head{font-family:"Montserrat",sans-serif;font-weight:800;}
  .body{font-family:"Roboto",sans-serif;}
  .year{font-family:"Montserrat",sans-serif;font-weight:800;font-size:19px;fill:#fff;}
  .label{font-family:"Roboto",sans-serif;font-size:12px;fill:var(--ink);}
  .small{font-family:"Roboto",sans-serif;font-size:7.4px;fill:var(--ink);}
  .col-title{font-family:"Roboto",sans-serif;font-weight:500;font-size:9px;fill:var(--ink);}
</style>
</head>
<body>
<svg class="canvas" viewBox="0 0 1068 986" width="1200" height="1108" xmlns="http://www.w3.org/2000/svg">
  <defs>
    <linearGradient id="dome-left" x1="0" x2="1">
      <stop offset="0" stop-color="#f2f7fc"/><stop offset="1" stop-color="#4f8fc9"/>
    </linearGradient>
    <linearGradient id="dome-right" x1="0" x2="1">
      <stop offset="0" stop-color="#e6f0fa"/><stop offset="1" stop-color="#3a7dc0"/>
    </linearGradient>
    <linearGradient id="ring-blue" x1="0" x2="1">
      <stop offset="0" stop-color="#5cc6ef"/><stop offset="1" stop-color="#1c7fc6"/>
    </linearGradient>
    <linearGradient id="soft-blue" x1="0" x2="1">
      <stop offset="0" stop-color="#cfe7f8"/><stop offset="1" stop-color="#8cc4ea"/>
    </linearGradient>
    <linearGradient id="core-blue" x1="0" x2="1">
      <stop offset="0" stop-color="#3e9be0"/><stop offset="1" stop-color="#52b1ea"/>
    </linearGradient>
    <linearGradient id="col-box" x1="0" x2="1">
      <stop offset="0" stop-color="#d7ecfb"/><stop offset="1" stop-color="#8ec7ee"/>
    </linearGradient>
    <linearGradient id="col-dark" x1="0" x2="1">
      <stop offset="0" stop-color="#0e3d62"/><stop offset="1" stop-color="#1d5f8f"/>
    </linearGradient>
    <filter id="lift" x="-30%" y="-30%" width="160%" height="160%">
      <feDropShadow dx="0" dy="2" stdDeviation="3" flood-color="#000" flood-opacity="0.25"/>
    </filter>
  </defs>

  <!-- Thinking modes -->
  <g class="thinking-modes">
    <path d="M121 237 A90 90 0 0 1 301 237 Z" fill="url(#dome-left)"/>
    <path d="M218 237 A90 90 0 0 1 398 237 Z" fill="url(#dome-right)" opacity="0.85"/>
    <rect x="121" y="233" width="277" height="7" rx="3.5" fill="var(--navy)"/>
    <text class="head" font-size="10" fill="var(--navy)" text-anchor="middle">
      <tspan x="177" y="200">ANALYTHIC</tspan><tspan x="177" y="213">THINKING</tspan>
    </text>
    <text class="head" font-size="10" fill="var(--red)" text-anchor="middle">
      <tspan x="261" y="200">DESIGN</tspan><tspan x="261" y="213">THINKING</tspan>
    </text>
    <text class="head" font-size="10" fill="var(--navy)" text-anchor="middle">
      <tspan x="344" y="193">INSTUITIVE &amp;</tspan><tspan x="344" y="206">CREATIVE</tspan><tspan x="344" y="219">THINKING</tspan>
    </text>
    <text class="head" font-size="7.5" fill="var(--ink)" text-anchor="middle" x="183" y="258">UNDERSTAND</text>
    <text class="head" font-size="13" fill="var(--ink)" text-anchor="middle" x="183" y="275">PROBLEM</text>
    <text class="head" font-size="7.5" fill="var(--ink)" text-anchor="middle" x="346" y="258">DESIGN</text>
    <text class="head" font-size="13" fill="var(--ink)" text-anchor="middle" x="346" y="275">SOLUTION</text>
    <path d="M242 265 L254 256 L254 261 L281 261 L281 256 L293 265 L281 274 L281 269 L254 269 L254 274 Z" fill="none" stroke="var(--red)" stroke-width="1.5" stroke-linejoin="round"/>
  </g>

  <!-- Contribution area -->
  <g class="contribution-area">
    <circle cx="682" cy="110" r="58" fill="none" stroke="url(#ring-blue)" stroke-width="22"/>
    <circle cx="906" cy="110" r="58" fill="none" stroke="url(#ring-blue)" stroke-width="22"/>
    <path d="M738 110 A58 58 0 0 1 854 110" fill="none" stroke="var(--red)" stroke-width="22"/>
    <circle cx="682" cy="110" r="46" fill="#fff" filter="url(#lift)"/>
    <circle cx="906" cy="110" r="46" fill="#fff" filter="url(#lift)"/>
    <circle cx="796" cy="110" r="48" fill="#fff" filter="url(#lift)"/>
    <text class="head" font-size="7.6" fill="var(--navy)" text-anchor="middle">
      <tspan x="682" y="97">DESIGN THINKING</tspan><tspan x="682" y="107">IN MANAGEMENT</tspan><tspan x="682" y="117">AND BUSINESS</tspan><tspan x="682" y="127">STRATGEY</tspan>
    </text>
    <text class="head" font-size="7.8" fill="var(--red)" text-anchor="middle">
      <tspan x="796" y="104">CONTRIBUTION</tspan><tspan x="796" y="114">AREA</tspan>
    </text>
    <text class="head" font-size="7.8" fill="var(--navy)" text-anchor="middle">
      <tspan x="906" y="98">RESEARCH</tspan><tspan x="906" y="108">THROUGH</tspan><tspan x="906" y="118">DESIGN - RID</tspan>
    </text>
  </g>

  <!-- Timeline -->
  <g class="timeline">
    <line x1="660" y1="305" x2="660" y2="356" stroke="var(--green)" stroke-width="3"/>
    <line x1="860" y1="305" x2="860" y2="356" stroke="var(--purple)" stroke-width="3"/>
    <line x1="552" y1="398" x2="552" y2="455" stroke="var(--yellow)" stroke-width="3"/>
    <line x1="757" y1="398" x2="757" y2="455" stroke="var(--cyan)" stroke-width="3"/>

    <polygon points="495,352 605,352 618,376 605,400 495,400 508,376" fill="var(--yellow)"/>
    <polygon points="603,352 708,352 721,376 708,400 603,400 616,376" fill="var(--green)"/>
    <polygon points="706,352 810,352 823,376 810,400 706,400 719,376" fill="var(--cyan)"/>
    <polygon points="808,352 912,352 925,376 912,400 808,400 821,376" fill="var(--purple)"/>
    <polygon points="910,352 1008,352 1021,376 1008,400 910,400 923,376" fill="var(--pink)"/>
    <text class="year" x="556" y="386" text-anchor="middle">2016</text>
    <text class="year" x="660" y="386" text-anchor="middle">2017</text>
    <text class="year" x="760" y="386" text-anchor="middle">2018</text>
    <text class="year" x="862" y="386" text-anchor="middle">2019</text>
    <text class="year" x="962" y="386" text-anchor="middle">2020</text>

    <path d="M612 260 A48 48 0 0 1 708 260" fill="none" stroke="var(--green)" stroke-width="3"/>
    <circle cx="660" cy="266" r="36" fill="var(--green)" stroke="#fff" stroke-width="4" role="img" aria-label="Icon: team meeting around a table"/>
    <path d="M812 260 A48 48 0 0 1 908 260" fill="none" stroke="var(--purple)" stroke-width="3"/>
    <circle cx="860" cy="266" r="36" fill="var(--purple)" stroke="#fff" stroke-width="4" role="img" aria-label="Icon: presentation to a group"/>
    <path d="M920 260 A48 48 0 0 1 1016 260" fill="none" stroke="var(--pink)" stroke-width="3"/>
    <circle cx="968" cy="266" r="36" fill="var(--pink)" stroke="#fff" stroke-width="4" role="img" aria-label="Icon: checklist with thumbs up"/>
    <path d="M504 500 A48 48 0 0 0 600 500" fill="none" stroke="var(--orange)" stroke-width="3"/>
    <circle cx="552" cy="495" r="38" fill="var(--yellow)" stroke="#fff" stroke-width="4" role="img" aria-label="Icon: students choosing an idea"/>
    <path d="M709 500 A48 48 0 0 0 805 500" fill="none" stroke="var(--cyan)" stroke-width="3"/>
    <circle cx="757" cy="495" r="38" fill="var(--cyan)" stroke="#fff" stroke-width="4" role="img" aria-label="Icon: online interview at a screen"/>

    <text class="label"><tspan x="517" y="306">Prequel with</tspan><tspan x="517" y="321">student-led</tspan><tspan x="517" y="336">innovation</tspan></text>
    <text class="label" x="729" y="332">Interventions</text>
    <text class="label"><tspan x="625" y="426">First Round of</tspan><tspan x="625" y="441">interviews</tspan></text>
    <text class="label"><tspan x="830" y="423">Secound</tspan><tspan x="830" y="438">Round of</tspan><tspan x="830" y="453">interviews</tspan></text>
    <text class="label"><tspan x="935" y="423">Additional</tspan><tspan x="935" y="438">interviews and</tspan><tspan x="935" y="453">comments</tspan></text>
  </g>

  <!-- Reflection -->
  <g class="reflection">
    <circle cx="225" cy="562" r="118" fill="none" stroke="var(--red)" stroke-width="13"/>
    <circle cx="207" cy="567" r="95" fill="url(#core-blue)"/>
    <circle cx="312" cy="518" r="50" fill="var(--blue-light)" opacity="0.85"/>
    <circle cx="312" cy="632" r="50" fill="var(--blue-light)" opacity="0.85"/>
    <g class="body" font-weight="700" font-size="8.6" fill="var(--ink)">
      <circle cx="148" cy="528" r="3.2"/><text x="158" y="531">Reflection involves</text><text x="158" y="543">three elements</text>
      <circle cx="148" cy="562" r="3.2"/><text x="158" y="565">Returing to experience</text>
      <circle cx="148" cy="585" r="3.2"/><text x="158" y="588">Attending to feeling</text>
      <circle cx="148" cy="608" r="3.2"/><text x="158" y="611">Evaluating experience</text>
    </g>
    <text class="body" font-weight="700" font-size="8.6" fill="var(--ink)" text-anchor="middle"><tspan x="321" y="514">Reflecting</tspan><tspan x="321" y="526">on action</tspan></text>
    <text class="body" font-weight="700" font-size="8.6" fill="var(--ink)" text-anchor="middle"><tspan x="316" y="629">Reflecting</tspan><tspan x="316" y="641">in action</tspan></text>
    <text class="body" font-size="7.8" fill="var(--ink)">
      <tspan x="357" y="559">Reflection is an active process</tspan><tspan x="357" y="569">of witnessing one's can</tspan><tspan x="357" y="579">experience in order to examine</tspan><tspan x="357" y="589">it more closely, give meaning to</tspan><tspan x="357" y="599">it, and learn from it.</tspan>
    </text>
  </g>

  <!-- Research overview -->
  <g class="research-overview">
    <rect x="382" y="605" width="684" height="376" fill="#fff" stroke="var(--frame)" stroke-width="3"/>
    <text class="col-title" x="403" y="659">POSITIONING THE RESEARCH</text>
    <text class="col-title" x="558" y="659">RESEARCH APPROACH</text>

    <ellipse cx="476" cy="740" rx="40" ry="62" fill="url(#soft-blue)"/>
    <ellipse cx="476" cy="862" rx="46" ry="78" fill="url(#soft-blue)"/>
    <ellipse cx="476" cy="770" rx="26" ry="32" fill="#5aaee4"/>
    <ellipse cx="476" cy="826" rx="33" ry="45" fill="var(--deep)"/>
    <circle cx="476" cy="803" r="18" fill="#1d6ca0"/>
    <g class="small" text-anchor="middle">
      <text><tspan x="472" y="709">Desing</tspan><tspan x="472" y="718">thinking</tspan></text>
      <text><tspan x="475" y="765">Design</tspan><tspan x="475" y="774">practice</tspan></text>
      <text font-size="10" x="476" y="807">CAP</text>
      <text fill="#fff"><tspan x="476" y="828">Theoretical</tspan><tspan x="476" y="837">approach to</tspan><tspan x="476" y="846">building design</tspan><tspan x="476" y="855">thinking</tspan><tspan x="476" y="864">capability</tspan></text>
      <text><tspan x="476" y="894">Design thinking</tspan><tspan x="476" y="903">in organization</tspan></text>
    </g>

    <text class="body" font-size="15" fill="var(--ink)" x="583" y="735" text-anchor="middle">RtD</text>
    <text class="small" text-anchor="middle"><tspan x="600" y="756">Learning dimension</tspan><tspan x="600" y="766">Pragmatic dimension</tspan></text>
    <path d="M513 776 L522 771 L522 774 L681 774 L681 771 L690 776 L681 781 L681 778 L522 778 L522 781 Z" fill="none" stroke="var(--red)" stroke-width="1.2"/>
    <rect x="522" y="775" width="159" height="3" fill="var(--red)"/>
    <polygon points="523,790 610,790 566,826" fill="#a8d6f2"/>
    <polygon points="610,790 697,790 653,826" fill="#a8d6f2"/>
    <polygon points="566,827 653,827 610,880" fill="#a8d6f2"/>
    <g class="small" text-anchor="middle">
      <text x="566" y="802">Design practice</text>
      <text x="652" y="802">Design studies</text>
      <text><tspan x="610" y="836">Design</tspan><tspan x="610" y="845">exploration</tspan></text>
    </g>

    <path d="M702 648 Q716 650 716 670 L716 780 Q716 795 728 797 Q716 799 716 814 L716 920 Q716 942 702 944" fill="none" stroke="var(--deep)" stroke-width="2.5"/>

    <text class="col-title" x="790" y="706" text-anchor="middle">METHODS</text>
    <text class="col-title" x="895" y="706" text-anchor="middle">FINDINGS</text>
    <text class="col-title" x="996" y="706" text-anchor="middle">CONTRIBUTION</text>

    <rect x="750" y="714" width="80" height="168" rx="9" fill="url(#col-box)" stroke="var(--muted)" stroke-width="3"/>
    <rect x="854" y="714" width="81" height="168" rx="9" fill="url(#col-dark)" stroke="#2f7fc0" stroke-width="3"/>
    <rect x="958" y="714" width="80" height="168" rx="9" fill="url(#col-box)" stroke="var(--muted)" stroke-width="3"/>

    <g class="small">
      <path d="M755 738 l3 2.5 l-3 2.5 Z M755 756 l3 2.5 l-3 2.5 Z M755 774 l3 2.5 l-3 2.5 Z M755 817 l3 2.5 l-3 2.5 Z M755 835 l3 2.5 l-3 2.5 Z M755 853 l3 2.5 l-3 2.5 Z" fill="var(--deep)"/>
      <text x="759" y="743">Interventions design</text>
      <text x="759" y="761">Reflection on action</text>
      <text><tspan x="759" y="779">Reflective</tspan><tspan x="759" y="788">conversation with</tspan><tspan x="759" y="797">the situation</tspan><tspan x="759" y="806">(reflection in action)</tspan></text>
      <text x="759" y="822">Proto- practices</text>
      <text x="759" y="840">Interviews</text>
      <text x="759" y="858">Observations</text>
    </g>
    <g class="small" fill="#fff">
      <path d="M859 732 l3 2.5 l-3 2.5 Z M859 765 l3 2.5 l-3 2.5 Z M859 811 l3 2.5 l-3 2.5 Z M859 838 l3 2.5 l-3 2.5 Z" fill="#7cc4f0"/>
      <text fill="#fff"><tspan x="864" y="737">The value of semi</tspan><tspan x="864" y="746">structured tools for</tspan><tspan x="864" y="755">non-designers</tspan></text>
      <text fill="#fff"><tspan x="864" y="770">Openness as a type</tspan><tspan x="864" y="779">of mindset</tspan><tspan x="864" y="788">supporting</tspan><tspan x="864" y="797">competence building</tspan></text>
      <text fill="#fff"><tspan x="864" y="816">The importance of</tspan><tspan x="864" y="825">insiders / experts</tspan></text>
      <text fill="#fff"><tspan x="864" y="843">The role of time</tspan><tspan x="864" y="852">during and between</tspan><tspan x="864" y="861">designs activates</tspan></text>
    </g>
    <g class="small">
      <path d="M962 744 l3 2.5 l-3 2.5 Z M962 782 l3 2.5 l-3 2.5 Z M962 834 l3 2.5 l-3 2.5 Z" fill="var(--deep)"/>
      <text><tspan x="967" y="749">Semi-structured and</tspan><tspan x="967" y="758">visual design tools</tspan><tspan x="967" y="767">(paper 1-4)</tspan></text>
      <text><tspan x="967" y="787">Framework of 3 core</tspan><tspan x="967" y="796">concepts dialogical</tspan><tspan x="967" y="805">space (paper 6)</tspan><tspan x="967" y="814">Temporality (paper 6)</tspan><tspan x="967" y="823">Openness (paper5)</tspan></text>
      <text x="967" y="839">Guidelines (paper7)</text>
    </g>
  </g>
</svg>
</body>
</html>
```